Entertainment Sound and Lighting company Business card

We need a professional looking business card designed for my growing entertainment sound and lighting company based in Sydney, Australia called "Kestrel Sound"

We provide technical production services (sound systems/lighting/vision) for events ranging from band gigs, weddings, corporate functions etc.

The business card needs to contain the following information:

Bartholomew Quenneville
Audio Engineer
Phone: 0478 615 702
Email: bartholomew@kestrelsound.com.au
Website: www.kestrelsound.com.au

Business logo has been attached in .ai format, please contact me if you need me to provide other files.

Target Market(s)

We need a business card that reflects our modern and professional company but still looks professional to appeal to our corporate clients.
We have a very broad target market spanning from bands needing PA systems for their gigs (18-30yrs) to event companies needing sound and lighting for weddings and other functions.

Industry/Entity Type

Business

Requirements
Must have
• Needs to include the logo that is attached of course, and the colour scheme.
Nice to have
• - Double sided

```html
<!DOCTYPE html>
<html lang="en">
<head>
<meta charset="utf-8">
<title>Kestrel Sound – Business Card</title>
<link rel="stylesheet" href="https://fonts.googleapis.com/css2?family=Comfortaa:wght@400;700&display=swap">
<style>
  :root {
    --page-bg: #e9eaeb;
    --card-white: #ffffff;
    --blue-deep: #0b5fc4;
    --blue-mid: #1a8fe0;
    --cyan-glow: #8ff2ee;
    --cyan: #45e6e6;
    --brand-blue: #1d86dc;
    --text-grey: #6b6f73;
    --rule-grey: #b9bcbf;
  }
  * { box-sizing: border-box; margin: 0; padding: 0; }
  html, body {
    width: 1001px;
    height: 1200px;
    overflow: hidden;
    background: var(--page-bg);
    font-family: "Comfortaa", sans-serif;
  }
  .canvas {
    position: relative;
    width: 1001px;
    height: 1200px;
  }
  .card {
    position: absolute;
    left: 70px;
    width: 860px;
    height: 488px;
    overflow: hidden;
  }
  /* Front */
  .card--front {
    top: 60px;
    background: radial-gradient(ellipse 48% 62% at 50% 40%, var(--cyan-glow) 0%, #4fc6ec 30%, var(--blue-mid) 62%, var(--blue-deep) 100%);
  }
  .front-brand {
    position: absolute;
    left: 0;
    right: 0;
    top: 205px;
    display: flex;
    align-items: center;
    justify-content: center;
    gap: 16px;
  }
  .front-brand__square {
    width: 22px;
    height: 22px;
    background: #ffffff;
  }
  .front-brand__name {
    font-size: 54px;
    font-weight: 700;
    color: #ffffff;
    letter-spacing: 0.5px;
  }
  /* Back */
  .card--back {
    top: 640px;
    background: var(--card-white);
  }
  .back-brand {
    position: absolute;
    left: 40px;
    top: 352px;
    display: flex;
    align-items: center;
    gap: 12px;
  }
  .back-brand__square {
    width: 18px;
    height: 18px;
    background: var(--cyan);
  }
  .back-brand__name {
    font-size: 38px;
    font-weight: 700;
    color: var(--brand-blue);
  }
  .back-divider {
    position: absolute;
    left: 388px;
    top: 340px;
    width: 1px;
    height: 78px;
    background: var(--rule-grey);
  }
  .person {
    position: absolute;
    left: 414px;
    top: 344px;
  }
  .person__name {
    font-size: 19px;
    color: var(--brand-blue);
    line-height: 1.1;
  }
  .person__role {
    font-size: 13px;
    color: var(--text-grey);
    margin-top: 2px;
  }
  .person__web {
    font-size: 18px;
    color: var(--text-grey);
    margin-top: 22px;
  }
  .contact-strip {
    position: absolute;
    left: 818px;
    top: 450px;
    transform-origin: left top;
    transform: rotate(-90deg);
    display: flex;
    align-items: center;
    gap: 10px;
    white-space: nowrap;
    font-size: 16px;
    color: var(--text-grey);
  }
  .contact-strip__dot {
    width: 10px;
    height: 10px;
    background: var(--cyan);
  }
  .back-band {
    position: absolute;
    left: 0;
    bottom: 0;
    width: 100%;
    height: 8px;
    background: linear-gradient(90deg, var(--blue-deep), var(--blue-mid) 45%, var(--cyan));
  }
</style>
</head>
<body>
<main class="canvas">
  <section class="card card--front" aria-label="Card front">
    <div class="front-brand">
      <span class="front-brand__square"></span>
      <span class="front-brand__name">Kestrel Sound</span>
    </div>
  </section>

  <section class="card card--back" aria-label="Card back">
    <div class="back-brand">
      <span class="back-brand__square"></span>
      <span class="back-brand__name">Kestrel Sound</span>
    </div>
    <div class="back-divider"></div>
    <div class="person">
      <p class="person__name">Bartholomew Quenneville</p>
      <p class="person__role">Audio Engineer</p>
      <p class="person__web">www.kestrelsound.com.au</p>
    </div>
    <div class="contact-strip">
      <span class="contact-strip__email">bartholomew@kestrelsound.com.au</span>
      <span class="contact-strip__dot"></span>
      <span class="contact-strip__phone">0478 615 702</span>
    </div>
    <div class="back-band"></div>
  </section>
</main>
</body>
</html>
```